New locally owned rental company needs a flyer to circulate

Need flyer with logo, phone# and address. We rent cars to anyone with driver's license and proper insurance. Rates as low as $50/day. Can offer compact cars, mid-size and full size sedans. Also SUV's.

```html
<!DOCTYPE html>
<html lang="en">
<head>
<meta charset="utf-8">
<title>DriveNest Rent a Car Flyer</title>
<link rel="stylesheet" href="https://fonts.googleapis.com/css2?family=Archivo+Black&family=Arimo:wght@400;700&display=swap">
<style>
  :root {
    --blue: #1d48a0;
    --blue-deep: #163a86;
    --green: #1e9b45;
    --green-light: #2bb052;
    --white: #ffffff;
    --paper: #f1f3f5;
    --ink: #1a1a1a;
    --grey-text: #4a4a4a;
    --stage: #58585a;
  }
  * { box-sizing: border-box; margin: 0; padding: 0; }
  html, body { width: 858px; height: 1200px; overflow: hidden; }
  body { background: var(--stage); font-family: "Arimo", Arial, sans-serif; }
  .flyer {
    position: absolute; left: 24px; top: 287px;
    width: 810px; height: 626px; overflow: hidden;
    background: var(--blue);
    box-shadow: 0 6px 18px rgba(0,0,0,.35);
  }
  .flyer-shapes { position: absolute; inset: 0; }
  .headline {
    position: absolute; left: 34px; top: 36px;
    font-family: "Archivo Black", Arial, sans-serif;
    font-size: 64px; line-height: 0.95; color: var(--white);
  }
  .headline .accent { color: var(--green-light); display: block; }
  .rate-line {
    position: absolute; left: 335px; top: 52px;
    font-family: "Archivo Black", Arial, sans-serif;
    font-size: 17px; color: var(--white); letter-spacing: .5px;
  }
  .price-pin {
    position: absolute; left: 512px; top: 122px; width: 106px; height: 130px;
  }
  .price-pin-label {
    position: absolute; left: 512px; top: 146px; width: 106px; text-align: center;
    font-family: "Archivo Black", Arial, sans-serif; color: var(--green);
  }
  .price-pin-label .amount { display: block; font-size: 30px; line-height: 1; }
  .price-pin-label .unit { display: block; font-family: "Arimo", Arial, sans-serif; font-weight: 700; font-size: 15px; color: var(--blue); }
  .info-column {
    position: absolute; right: 22px; top: 48px; width: 200px; text-align: right;
  }
  .info-title {
    font-family: "Archivo Black", Arial, sans-serif; font-size: 24px; line-height: 1;
    color: var(--blue);
  }
  .info-title .accent { display: block; color: var(--green); }
  .offer-list { list-style: none; margin: 10px 0 0; }
  .offer-list li {
    font-weight: 700; font-size: 13px; line-height: 19px; color: var(--grey-text);
  }
  .offer-list li::after { content: "•"; color: var(--green); margin-left: 7px; }
  .who-can-rent { margin-top: 30px; }
  .who-can-rent p {
    margin-top: 12px; font-weight: 700; font-size: 13px; line-height: 19px; color: var(--grey-text);
  }
  .brand {
    position: absolute; left: 58px; top: 540px;
  }
  .brand-name {
    font-family: "Archivo Black", Arial, sans-serif; font-size: 44px; line-height: 1;
    color: var(--blue); letter-spacing: -1px;
  }
  .brand-tagline {
    margin-top: 6px; margin-left: 26px;
    font-family: "Archivo Black", Arial, sans-serif; font-size: 17px; letter-spacing: 7px; color: var(--ink);
  }
  .divider { position: absolute; left: 408px; top: 540px; width: 1px; height: 66px; background: #9a9a9a; }
  .contact { position: absolute; left: 430px; top: 540px; }
  .phone {
    position: relative; display: flex; align-items: center; gap: 10px;
    width: 242px; height: 30px; padding-left: 4px;
    background: var(--ink); border-radius: 15px;
    font-family: "Archivo Black", Arial, sans-serif; font-size: 22px; color: var(--white);
  }
  .phone-icon { width: 30px; height: 30px; margin-left: -6px; }
  .address {
    margin-top: 8px; font-weight: 700; font-size: 13px; line-height: 16px; color: var(--grey-text); letter-spacing: .6px;
  }
</style>
</head>
<body>
  <main class="flyer">
    <svg class="flyer-shapes" width="810" height="626" viewBox="0 0 810 626" aria-hidden="false">
      <defs>
        <linearGradient id="car-tone" x1="0" y1="0" x2="0" y2="1">
          <stop offset="0" stop-color="#e6e6e2"/>
          <stop offset="0.6" stop-color="#c7c7c2"/>
          <stop offset="1" stop-color="#6d6d6d"/>
        </linearGradient>
        <linearGradient id="lot-tone" x1="0" y1="0" x2="1" y2="0">
          <stop offset="0" stop-color="#4aa862"/>
          <stop offset="1" stop-color="#1e9b45"/>
        </linearGradient>
      </defs>
      <polygon class="panel-white" points="325,0 810,0 810,370 668,626 15,626" fill="var(--paper)"/>
      <g role="img" aria-label="Photo of the rental lot with parked cars, tinted green">
        <polygon class="panel-green" points="330,0 685,0 545,262 215,262" fill="url(#lot-tone)"/>
      </g>
      <polygon class="corner-blue" points="810,360 810,626 665,626" fill="var(--blue-deep)"/>
      <g role="img" aria-label="Photo of a silver mid-size sedan">
        <rect x="44" y="188" width="550" height="180" rx="70" fill="url(#car-tone)"/>
      </g>
      <g class="photo-strip">
        <polygon points="22,500 58,400 220,400 184,500" fill="#fff"/>
        <g role="img" aria-label="Photo of a blue compact car"><polygon points="30,494 62,406 212,406 180,494" fill="#3a4fb0"/></g>
        <polygon points="208,500 244,400 406,400 370,500" fill="#fff"/>
        <g role="img" aria-label="Photo of a grey SUV"><polygon points="216,494 248,406 398,406 366,494" fill="#6b7078"/></g>
        <polygon points="394,500 430,400 592,400 556,500" fill="#fff"/>
        <g role="img" aria-label="Photo of a red mid-size sedan"><polygon points="402,494 434,406 584,406 552,494" fill="#b8283c"/></g>
        <polygon points="580,500 616,400 790,400 754,500" fill="#fff"/>
        <g role="img" aria-label="Photo of a silver SUV"><polygon points="588,494 620,406 782,406 750,494" fill="#a9adb2"/></g>
      </g>
      <polygon points="512,170 618,170 565,252" fill="var(--blue)"/>
      <circle cx="565" cy="175" r="53" fill="var(--blue)"/>
      <circle cx="565" cy="175" r="44" fill="var(--white)"/>
    </svg>

    <h1 class="headline"><span class="accent">RENT</span>A CAR</h1>
    <p class="rate-line">RATES AS LOW AS $50/DAY</p>

    <div class="price-pin-label"><span class="amount">$50</span><span class="unit">PER DAY</span></div>

    <aside class="info-column">
      <section class="offers">
        <h2 class="info-title">OUR<span class="accent">OFFERS</span></h2>
        <ul class="offer-list">
          <li>COMPACT CARS</li>
          <li>MID-SIZE</li>
          <li>ULL SIZE SEDANS</li>
          <li>SUV'S</li>
        </ul>
      </section>
      <section class="who-can-rent">
        <h2 class="info-title">WHO CAN<span class="accent">RENT</span></h2>
        <p>WE RENT CARS TO ANYONE WITH DRIVER'S LICENSE AND PROPER INSURANCE.</p>
      </section>
    </aside>

    <div class="brand">
      <div class="brand-name">DriveNest</div>
      <div class="brand-tagline">Car &amp; Van Rental</div>
    </div>
    <div class="divider"></div>
    <div class="contact">
      <div class="phone">
        <svg class="phone-icon" viewBox="0 0 30 30" aria-hidden="true">
          <circle cx="15" cy="15" r="14" fill="var(--green-light)" stroke="#fff" stroke-width="2"/>
          <path d="M10 8.5c1-.6 2-.3 2.4.7l1 2.3c.3.7 0 1.4-.6 1.8l-.9.6c.8 1.8 2.2 3.2 4 4l.6-.9c.4-.6 1.1-.9 1.8-.6l2.3 1c1 .4 1.3 1.4.7 2.4-.9 1.5-2.6 2-4.2 1.3-3.4-1.4-6.1-4.1-7.5-7.5-.7-1.6-.2-3.3 1.3-4.2z" fill="#fff"/>
        </svg>
        555-014-2736
      </div>
      <p class="address">4180 Maple Crest Avenue<br>Riverton, AL 35000</p>
    </div>
  </main>
</body>
</html>
```